Need updated stationery design for chiropractic clinic

We recently moved our office and are looking to refresh our letterhead, business cards, presentation folder and envelopes. I tend to prefer simple, clean designs. We communicate with a lot of attorneys and want to exude professionalism. I have attached our logo and 2 additional versions (all white and white letters instead of grey).

Target Market(s)

Other medical professionals and attorneys. Business cards will go to patients as well.

Industry/Entity Type

Healthcare

```html
<!DOCTYPE html>
<html lang="en">
<head>
<meta charset="utf-8">
<title>Alignwell Injury Care Clinic – Business Card</title>
<link href="https://fonts.googleapis.com/css2?family=Roboto:wght@400;700&display=swap" rel="stylesheet">
<style>
  :root {
    --backdrop: #d4d7d8;
    --card: #f3f3f1;
    --brand-blue: #1b6db0;
    --brand-teal: #2aa3a0;
    --ink: #3a3a3a;
    --ink-soft: #555;
  }
  * { box-sizing: border-box; margin: 0; padding: 0; }
  html, body {
    width: 1200px; height: 1050px; overflow: hidden;
    background: var(--backdrop);
    font-family: "Roboto", Arial, sans-serif;
  }
  .sheet {
    width: 1200px; height: 1050px;
    display: flex; flex-direction: column; align-items: center; justify-content: center;
    gap: 40px;
  }
  .card {
    position: relative;
    width: 820px; height: 469px;
    background: var(--card);
    border-bottom: 5px solid var(--brand-blue);
    box-shadow: 0 10px 24px rgba(0,0,0,0.12);
  }
  .brand {
    position: absolute;
    display: flex; align-items: center; gap: 14px;
  }
  .brand-mark {
    width: 30px; height: 30px; flex: none;
    background: var(--brand-blue);
  }
  .brand-name {
    font-weight: 700; color: var(--brand-blue);
    line-height: 1.05; font-size: 40px;
  }
  .brand-name small { display: block; font-size: 22px; letter-spacing: 1px; font-weight: 700; }

  /* Front: contact side */
  .card-front .brand { top: 92px; right: 62px; }
  .holder { position: absolute; top: 86px; left: 62px; }
  .holder-name { font-size: 26px; font-weight: 700; color: var(--brand-blue); letter-spacing: 0.5px; }
  .holder-title { font-size: 19px; color: var(--brand-teal); margin-top: 2px; }
  .rule {
    position: absolute; top: 178px; left: 290px; width: 468px;
    height: 1.5px; background: var(--brand-teal);
  }
  .contacts { position: absolute; top: 192px; left: 62px; list-style: none; }
  .contacts li {
    display: flex; align-items: center; gap: 10px;
    font-size: 21px; color: var(--ink-soft); height: 34px;
  }
  .contacts svg { width: 20px; height: 20px; flex: none; }
  .address {
    position: absolute; right: 62px; bottom: 58px;
    text-align: right; font-size: 20px; line-height: 1.4; color: var(--ink);
  }

  /* Back: brand side */
  .card-back .brand { top: 160px; left: 50%; transform: translateX(-50%); }
  .card-back .brand-name { font-size: 50px; }
  .card-back .brand-name small { font-size: 27px; }
  .card-back .brand-mark { width: 38px; height: 38px; }
  .back-web {
    position: absolute; top: 330px; width: 100%; text-align: center;
    font-size: 20px; color: var(--ink-soft);
  }
</style>
</head>
<body>
<main class="sheet">
  <section class="card card-front" aria-label="Business card, contact side">
    <div class="brand">
      <span class="brand-mark" aria-hidden="true"></span>
      <div class="brand-name">Alignwell<small>Injury Care Clinic</small></div>
    </div>
    <div class="holder">
      <div class="holder-name">DANIEL REYES</div>
      <div class="holder-title">Founder &amp; CEO</div>
    </div>
    <div class="rule" aria-hidden="true"></div>
    <ul class="contacts">
      <li>
        <svg viewBox="0 0 24 24" aria-hidden="true"><path fill="var(--brand-blue)" d="M6.6 10.8a15.1 15.1 0 0 0 6.6 6.6l2.2-2.2a1 1 0 0 1 1-.25 11.4 11.4 0 0 0 3.6.57 1 1 0 0 1 1 1V20a1 1 0 0 1-1 1A17 17 0 0 1 3 4a1 1 0 0 1 1-1h3.5a1 1 0 0 1 1 1c0 1.25.2 2.45.57 3.57a1 1 0 0 1-.25 1z"/></svg>
        (555) 318-4420
      </li>
      <li>
        <svg viewBox="0 0 24 24" aria-hidden="true"><rect x="2.5" y="5" width="19" height="14" fill="none" stroke="var(--brand-blue)" stroke-width="1.8"/><path d="M2.5 5l9.5 8 9.5-8" fill="none" stroke="var(--brand-blue)" stroke-width="1.8"/></svg>
        info@alignwellclinic.com
      </li>
      <li>
        <svg viewBox="0 0 24 24" aria-hidden="true"><g fill="none" stroke="var(--brand-blue)" stroke-width="1.6"><circle cx="12" cy="12" r="9"/><ellipse cx="12" cy="12" rx="4" ry="9"/><path d="M3 12h18M5 7h14M5 17h14"/></g></svg>
        www.alignwellclinic.com
      </li>
    </ul>
    <address class="address" style="font-style:normal">
      Alignwell Injury Care Clinic<br>
      48 Harbor Lane, Suite 3<br>
      Linwood, MA 01990
    </address>
  </section>

  <section class="card card-back" aria-label="Business card, brand side">
    <div class="brand">
      <span class="brand-mark" aria-hidden="true"></span>
      <div class="brand-name">Alignwell<small>Injury Care Clinic</small></div>
    </div>
    <div class="back-web">www.alignwellclinic.com</div>
  </section>
</main>
</body>
</html>
```